Stock Broking Firm - Web Design Project

We are looking at doing a full re-design of our home page and content page and moving the majority of our content over to DNN.

Phase 1 : Website redesign www.kalvernequities.com.au

The current design is too washed out, boring and has no call to action buttons.

Solution:

KL Equities is looking for a brighter/ cleaner redesign with a few stand out call to action buttons.

• Banner with logo across the top horizontally - Bright blue logo on white background similar to www.dmq.com.au - CALL 1300 482 917 - Follow on Chirper / Facespace
• Horizontal menu bar - professional looking. - Home - About Us- Our Services - Membership - Open an Account - Become a member - Contact
• Below banner top left - large rotating banner - maybe zimbo gallery style www.tvhaldrens.com.au
• Right of rotating banner - Membership login
• Below members login - Register for Daily Market Report/ research blog - Large bright button / Name / Email / Phone / pop up??
• Below Register for daily market report - Market Indicies - RSS feed of delayed data from QNW see www.tvhaldrens.com
• Below Market indicies - KL EQUITIES - Market Tweets ( feed from our chirper page)

Below Rotating Banner -

content area

Below content area - 4 large block buttons see www.crandwickley.com.au ( hover over change colour)

Button 1 - EDUCATION - content - click here for more

Button 2 - Market Information and Research

Button 3 - Full service Broker - content brief - click here for more

Button 4 - Trade Commodities and Options

below buttons - small horizontal menu bar slightly different colour incl - Careers/ Partners / Legal Privacy FSG Site Map

Regards,
Colin Marsh

Target Market(s)

35 - 65

Industry/Entity Type

Education

Requirements
Must have
• Follow brief above - large banner, call to action buttons, F.S. Chirper, Member login etc. 4 big buttons
Nice to have
• clean looking site similar to www.dmq.com.au / not too busy. Corporate looking.
Should not have
• not too busy

```html
<!DOCTYPE html>
<html lang="en">
<head>
<meta charset="utf-8">
<title>KL Equities</title>
<link rel="stylesheet" href="https://fonts.googleapis.com/css2?family=Open+Sans:wght@400;600&family=Arimo:wght@400;700&display=swap">
<style>
:root{
  --blue:#1a73d1;
  --blue-dark:#0d5bb5;
  --blue-light:#27a4f0;
  --navy:#1a4e8f;
  --charcoal:#3f3f3f;
  --ink:#444;
  --muted:#666;
  --line:#dcdcdc;
  --page:#f2f2f2;
  --neg:#c42a2a;
  --row:#e6edf8;
}
*{box-sizing:border-box;margin:0;padding:0}
html,body{width:1113px;height:1200px;overflow:hidden;background:#fff}
.stage{position:absolute;left:0;top:0;width:1280px;height:1380px;transform:scale(.86953);transform-origin:0 0;font-family:"Arimo",Arial,sans-serif;color:var(--ink);background:linear-gradient(#fff 0,#fff 497px,var(--page) 497px)}
.abs{position:absolute}
.head-band{left:0;top:0;width:1280px;height:57px;background:linear-gradient(#fff,#eef0f2)}
.brand{left:155px;top:6px;display:flex;align-items:center;gap:10px;font-family:"Open Sans",sans-serif;font-size:42px;color:var(--blue);line-height:44px}
.brand-mark{width:42px;height:42px;background:var(--blue);border-radius:50%}
.phone{left:773px;top:17px;display:flex;align-items:center;gap:6px;font-family:"Open Sans",sans-serif;font-size:26px;color:#666}
.social{display:flex;gap:6px}
.social span{display:block;width:22px;height:22px;border-radius:50%;background:#fff;border:2px solid var(--blue-light)}
.nav-band{left:0;top:57px;width:1280px;height:56px;background:linear-gradient(#2a8fe0,#1365c8)}
.nav{left:135px;top:57px;height:56px;display:flex;font-family:"Open Sans",sans-serif;font-size:15px;color:#fff}
.nav a{display:flex;align-items:center;justify-content:center;color:#fff;text-decoration:none;height:56px}
.nav a:nth-child(odd){background:linear-gradient(#2fb1f7,#1d94ec)}
.nav a:nth-child(even){background:linear-gradient(#1b7ee0,#1367cc)}
.nav a:first-child{justify-content:flex-start;padding-left:24px}
.slide{left:135px;top:113px;width:652px;height:284px;background:linear-gradient(90deg,#ddd6cf,#bfb2a6 60%,#ece8e4)}
.arrow-btn{width:44px;height:44px;border-radius:50%;background:rgba(80,80,80,.35);display:flex;align-items:center;justify-content:center}
.caption{left:135px;top:397px;width:652px;height:92px;background:var(--blue)}
.caption h2{position:absolute;left:23px;top:10px;font-family:"Open Sans",sans-serif;font-weight:400;font-size:21px;color:#fff}
.caption p{position:absolute;left:23px;top:39px;width:410px;font-size:11.5px;line-height:14px;color:#e6f1ff}
.thumb{position:absolute;width:67px;height:33px;border:1px solid #fff}
.login{left:793px;top:113px;width:323px;height:188px;background:linear-gradient(135deg,#1b6ad0,#0c4fae)}
.login h3,.report h3{position:absolute;font-family:"Open Sans",sans-serif;font-weight:400;font-size:21px}
.login h3{left:26px;top:16px;color:#fff}
.lock{right:12px;top:8px;width:90px;height:110px;border-radius:40% 40% 20% 20%;background:radial-gradient(circle at 50% 65%,#5fa4ea,#2e7dd6 70%,transparent 72%)}
.field-label{position:absolute;font-size:12px}
.login .field-label{color:#d8e8ff;left:26px}
.login .input{position:absolute;left:98px;width:197px;height:29px;background:#2ea3f2}
.forgot{position:absolute;left:109px;top:139px;font-size:11.5px;color:#fff;text-decoration:underline}
.btn-white{position:absolute;height:27px;background:linear-gradient(#fff,#e6e6e6);border:1px solid #bbb;font-size:12px;font-weight:700;color:var(--navy);display:flex;align-items:center;justify-content:center}
.report{left:793px;top:301px;width:323px;height:188px;background:#fff;border:1px solid var(--line)}
.report h3{left:25px;top:16px;color:var(--navy)}
.report .field-label{color:#444;left:27px}
.report .input{position:absolute;left:97px;width:198px;height:30px;border:1px solid #ccc;background:linear-gradient(#fff,#f1f1f1)}
.card{width:320px;background:#fff;border:1px solid var(--line)}
.card-head{height:43px;background:linear-gradient(90deg,var(--blue-dark) 0,var(--blue-dark) 74%,#2e7ed8 74%,#2e7ed8 87%,#2b8ae4 87%);font-family:"Open Sans",sans-serif;font-size:21px;color:#fff;padding:6px 0 0 22px;white-space:nowrap;overflow:hidden}
.card-head.wide{padding-left:18px;font-size:20px}
.card-head.narrow{padding:9px 0 0 18px;font-size:17.5px}
.card h4{position:absolute;left:22px;top:62px;font-size:12px;font-weight:700;color:#444}
.card p{position:absolute;left:23px;width:148px;font-size:12px;line-height:18.7px;color:#666}
.icon-disc{position:absolute;width:115px;height:115px;border-radius:50%;background:var(--charcoal);display:flex;align-items:center;justify-content:center}
.read-more{position:absolute;left:22px;width:277px;height:29px;background:linear-gradient(90deg,#e2e2e2,#c9c9c9 90%);font-size:14px;color:#333;display:flex;align-items:center;padding-left:20px}
.read-more i{position:absolute;right:0;top:0;width:64px;height:29px;background:linear-gradient(90deg,var(--blue) 50%,#1e7fe0 50%);display:flex;align-items:center;justify-content:flex-end;padding-right:10px}
.side-head{height:43px;display:flex;align-items:center;gap:14px;padding-left:12px;font-family:"Open Sans",sans-serif;font-size:21px;color:#fff}
.side-head.dark{background:linear-gradient(#6b6b6b,#2e2e2e)}
.side-head.blue{background:linear-gradient(#2a7fdb,#0d4fae)}
.side-head b{width:26px;height:26px;border-radius:50%;background:#fff;display:block}
.side-box{left:793px;width:323px;background:#fff;border:1px solid var(--line)}
.market-table{margin:10px 6px 0;width:311px;border-collapse:collapse;font-size:11px}
.market-table th{text-align:left;font-weight:700;color:#333;height:26px}
.market-table td{height:24px;color:#333;border-top:1px solid #fff}
.market-table tbody tr:nth-child(odd){background:var(--row)}
.market-table tbody tr:nth-child(even){background:#f5f8fc}
.market-table .neg{color:var(--neg)}
.post{position:absolute;left:15px;width:292px;font-size:11.5px}
.post h5{font-size:11.5px;font-weight:700;color:#444;width:200px;line-height:14px}
.post time{position:absolute;right:0;top:0;color:#666}
.post p{margin-top:12px;color:#666;line-height:14.4px}
.divider{position:absolute;left:15px;width:292px;border-top:1px dashed #bbb}
.tweet{position:absolute;left:17px;width:287px;height:56px;background:#f5f5f5;border-bottom:1px solid #fff}
.tweet .avatar{position:absolute;left:8px;top:12px;width:40px;height:40px;background:linear-gradient(#c9b9a7,#8f7f70)}
.tweet .who{position:absolute;left:59px;top:13px;font-size:12px;color:#2b88d8}
.tweet .where{position:absolute;left:59px;top:32px;font-size:12px;color:#444}
.tweet .where span{color:#2b88d8}
.partners{left:135px;top:1138px;width:652px;height:155px;background:#fff;border:1px solid var(--line)}
.partner-row{position:absolute;left:20px;top:73px;display:flex;gap:26px;align-items:center}
.partner-row span{display:block;width:78px;height:30px;border-radius:4px;background:#d9d9d9}
.footer{left:0;top:1320px;width:1280px;height:60px;background:linear-gradient(#2c8ee2,#1664c6)}
.footer-links{left:131px;top:1341px;font-size:12px;color:#fff;word-spacing:2px}
.footer-copy{left:799px;top:1341px;font-size:12px;color:#fff}
.footer-social{left:547px;top:1335px;display:flex;gap:2px}
.footer-social span{width:26px;height:26px;border-radius:50%;background:#fff;display:block}
</style>
</head>
<body>
<div class="stage">
  <div class="abs head-band"></div>
  <div class="abs brand"><span class="brand-mark"></span>KL Equities</div>
  <div class="abs phone">
    <svg width="26" height="26" viewBox="0 0 26 26"><circle cx="13" cy="13" r="13" fill="#2b8ae4"/><path d="M9 6c1 0 2 3 2 4s-2 1-1 3 3 4 4 4 1-2 2-2 4 1 4 2-2 3-4 3-6-2-8-6-1-8 1-8z" fill="#fff"/></svg>
    1300 482 917
    <div class="social" style="margin-left:18px"><span></span><span></span><span></span><span></span></div>
  </div>

  <div class="abs nav-band"></div>
  <nav class="abs nav">
    <a style="width:98px">Home</a><a style="width:100px">About Us</a><a style="width:142px">Our Services</a><a style="width:139px">Membership</a><a style="width:173px">Open an Account</a><a style="width:196px">Become a member</a><a style="width:133px">Contact</a>
  </nav>

  <div class="abs slide" role="img" aria-label="Photo of a smiling businesswoman in front of a team of colleagues"></div>
  <div class="abs arrow-btn" style="left:143px;top:270px"><svg width="12" height="16"><path d="M9 2 3 8l6 6" stroke="#fff" stroke-width="2" fill="none"/></svg></div>
  <div class="abs arrow-btn" style="left:734px;top:270px"><svg width="12" height="16"><path d="M3 2l6 6-6 6" stroke="#fff" stroke-width="2" fill="none"/></svg></div>
  <div class="abs caption">
    <h2>HIGHER POTENTIAL RETURN</h2>
    <p>Trading options on Australian stocks or commodities such as gold and silver, you spend much less money and make almost the same profit as if you buy or sell Australian stocks.</p>
    <div class="thumb" style="left:496px;top:12px;background:#cfc6bd" role="img" aria-label="Team photo thumbnail"></div>
    <div class="thumb" style="left:568px;top:12px;background:#e6e6e6" role="img" aria-label="Business people thumbnail"></div>
    <div class="thumb" style="left:496px;top:51px;background:#b9bcc0" role="img" aria-label="World map thumbnail"></div>
    <div class="thumb" style="left:568px;top:51px;background:#f4f4f4" role="img" aria-label="Rising chart thumbnail"></div>
  </div>

  <section class="abs login">
    <h3>Members Login</h3>
    <div class="abs lock" role="img" aria-label="Padlock illustration"></div>
    <span class="field-label" style="top:67px">Username</span><div class="input" style="top:60px"></div>
    <span class="field-label" style="top:104px">Password</span><div class="input" style="top:96px"></div>
    <span class="forgot">Forget password?</span>
    <div class="btn-white" style="left:224px;top:132px;width:72px">Login</div>
  </section>

  <section class="abs report">
    <h3>Daily Market Report</h3>
    <span class="field-label" style="top:64px">Name</span><div class="input" style="top:58px"></div>
    <span class="field-label" style="top:103px">Email</span><div class="input" style="top:96px"></div>
    <div class="btn-white" style="left:190px;top:134px;width:107px;height:29px">Register</div>
  </section>

  <article class="abs card" style="left:135px;top:503px;height:310px">
    <div class="card-head">Education</div>
    <h4>Get Education info from here</h4>
    <p style="top:89px">Lorem ipsum dolor sit amet, consectetuer adipiscing elit, sed diam nonummy nibh euismod tincidunt ut laoreet dolore magna aliqlobortis nisl ut aliquip ex ea commodo consequat.</p>
    <div class="icon-disc" style="left:188px;top:63px"><svg width="60" height="40" viewBox="0 0 60 40" fill="#fff"><circle cx="30" cy="9" r="7"/><path d="M18 38c0-10 5-16 12-16s12 6 12 16z"/><circle cx="14" cy="13" r="5"/><path d="M4 36c0-8 4-12 10-12 2 0 4 1 5 2-2 3-3 6-3 10z"/><circle cx="46" cy="13" r="5"/><path d="M56 36c0-8-4-12-10-12-2 0-4 1-5 2 2 3 3 6 3 10z"/></svg></div>
    <div class="read-more" style="top:264px">Read More<i><svg width="10" height="16"><path d="M2 1l6 7-6 7" stroke="#fff" stroke-width="1.6" fill="none"/></svg></i></div>
  </article>

  <article class="abs card" style="left:467px;top:503px;height:310px">
    <div class="card-head wide">Market Info and Research</div>
    <h4 style="left:18px">Get Market info from here</h4>
    <p style="top:97px;left:18px;width:170px">Lorem ipsum dolor sit amet, consectetuer adipiscing elit, sed diam nonummy nibh euismod tincidunt ut laoreet dolore magna aliqlobortis nisl ut aliquip ex ea commodo consequat.</p>
    <div class="icon-disc" style="left:193px;top:63px"><svg width="54" height="36" viewBox="0 0 54 36"><rect x="7" y="3" width="40" height="26" rx="2" fill="none" stroke="#fff" stroke-width="3"/><path d="M1 31h52v3H1z" fill="#fff"/></svg></div>
    <div class="read-more" style="top:264px;left:20px">Read More<i><svg width="10" height="16"><path d="M2 1l6 7-6 7" stroke="#fff" stroke-width="1.6" fill="none"/></svg></i></div>
  </article>

  <article class="abs card" style="left:135px;top:819px;height:310px">
    <div class="card-head">Full Service Broker</div>
    <h4>Get Education info from here</h4>
    <p style="top:93px">Lorem ipsum dolor sit amet, consectetuer adipiscing elit, sed diam nonummy nibh euismod tincidunt ut laoreet dolore magna aliqlobortis nisl ut aliquip ex ea commodo consequat.</p>
    <div class="icon-disc" style="left:184px;top:60px"><svg width="48" height="48" viewBox="0 0 48 48"><circle cx="24" cy="24" r="20" fill="none" stroke="#fff" stroke-width="4"/><path d="M24 10v16" stroke="#fff" stroke-width="4"/><circle cx="24" cy="27" r="4" fill="#fff"/></svg></div>
    <div class="read-more" style="top:266px">Read More<i><svg width="10" height="16"><path d="M2 1l6 7-6 7" stroke="#fff" stroke-width="1.6" fill="none"/></svg></i></div>
  </article>

  <article class="abs card" style="left:467px;top:819px;height:310px">
    <div class="card-head narrow">Trade Commodities and Options</div>
    <h4 style="left:18px">Get Market info from here</h4>
    <p style="top:102px;left:18px;width:170px">Lorem ipsum dolor sit amet, consectetuer adipiscing elit, sed diam nonummy nibh euismod tincidunt ut laoreet dolore magna aliqlobortis nisl ut aliquip ex ea commodo consequat.</p>
    <div class="icon-disc" style="left:193px;top:60px"><svg width="46" height="46" viewBox="0 0 46 46"><g fill="#fff"><circle cx="23" cy="23" r="14"/><rect x="19" y="2" width="8" height="42" rx="2"/><rect x="19" y="2" width="8" height="42" rx="2" transform="rotate(45 23 23)"/><rect x="19" y="2" width="8" height="42" rx="2" transform="rotate(90 23 23)"/><rect x="19" y="2" width="8" height="42" rx="2" transform="rotate(135 23 23)"/></g><circle cx="23" cy="23" r="6" fill="#3f3f3f"/></svg></div>
    <div class="read-more" style="top:266px;left:20px">Read More<i><svg width="10" height="16"><path d="M2 1l6 7-6 7" stroke="#fff" stroke-width="1.6" fill="none"/></svg></i></div>
  </article>

  <section class="abs side-box" style="top:503px;height:210px">
    <div class="side-head dark"><b></b>Market Report</div>
    <table class="market-table">
      <thead><tr><th style="width:86px">Name</th><th style="width:88px">Value</th><th style="width:62px">+/-</th><th>%+/-</th></tr></thead>
      <tbody>
        <tr><td>Broad Idx</td><td>4,511.90</td><td class="neg">-14.70</td><td class="neg">-0.32</td></tr>
        <tr><td>Top 200</td><td>4,490.74</td><td class="neg">-14.56</td><td class="neg">-0.32</td></tr>
        <tr><td>Ind 30</td><td>13,473.53</td><td class="neg">-110.12</td><td class="neg">-0.81</td></tr>
        <tr><td>Harbour</td><td>20,919.60</td><td class="neg">-17.68</td><td class="neg">-0.08</td></tr>
        <tr><td>TechCmp</td><td>3,065.02</td><td class="neg">-47.33</td><td class="neg">-1.52</td></tr>
      </tbody>
    </table>
  </section>

  <section class="abs side-box" style="top:724px;height:331px">
    <div class="side-head blue"><b></b>Research Blog</div>
    <div class="post" style="top:57px"><h5>$A down after GFO lowers growth forecasts</h5><time>04:46 PM</time><p>Lorem ipsum dolor sit amet, consectetuer adipiscing elit, sed diam nonummy nibh euismod tincidunt ut laoreet dolore magna aliqlobortis nisl ut aliquip ex ea commodo consequat.</p></div>
    <div class="divider" style="top:169px"></div>
    <div class="post" style="top:189px"><h5>$A down after GFO lowers growth forecasts</h5><time>04:23 PM</time><p>Lorem ipsum dolor sit amet, consectetuer adipiscing elit, sed diam nonummy nibh euismod tincidunt ut laoreet dolore magna aliquam erat volutpat. Ut wisi enim ad minim veniam, quis nostrud exerci tation ullamcorper suscipit lobortis nisl ut aliquip ex ea commodo consequat.</p></div>
  </section>

  <section class="abs side-box" style="top:1061px;height:237px">
    <div class="side-head dark"><b></b>Chirper feeds</div>
    <div class="tweet" style="top:48px"><div class="avatar" role="img" aria-label="User avatar"></div><span class="who">helen2012</span><span class="where">Posted on <span>Clear Thinking Caps</span></span></div>
    <div class="tweet" style="top:104px"><div class="avatar" role="img" aria-label="User avatar"></div><span class="who">Super User</span><span class="where">Posted on <span>Riverside Football Fans</span></span></div>
    <div class="tweet" style="top:160px"><div class="avatar" role="img" aria-label="User avatar"></div><span class="who">Marco Veltri</span><span class="where">Posted on <span>Angak Notes</span></span></div>
  </section>

  <section class="abs partners">
    <div class="side-head dark" style="padding-left:23px">Partners</div>
    <div class="partner-row"><span></span><span></span><span></span><span></span><span></span><span></span></div>
  </section>

  <footer>
    <div class="abs footer"></div>
    <div class="abs footer-links">Careers | Partners | Legal Privacy | FSG Site Map</div>
    <div class="abs footer-social"><span></span><span></span><span></span><span></span></div>
    <div class="abs footer-copy">© 2012 KL Equities (QLD) Pty Ltd, All Rights Reserved.</div>
  </footer>
</div>
</body>
</html>
```